Trevik Builders Business Card Design Project

Clean sharp business card
Ability to write on back of card
Details for the card -
Address: PO Box 5087, Corrabeen, Qld, 4286
ABN: 47 305 921 276
BSA LIC 6825170
Ph: 07 4651 2839
Fax: 07 4651 2840
Email: trevikbuilders@quillpost.net

Reason: Time to review designs after weekend

```html
<!DOCTYPE html>
<html lang="en">
<head>
<meta charset="utf-8">
<title>Trevik Builders – Business Card</title>
<link href="https://fonts.googleapis.com/css2?family=Cinzel:wght@400;600&display=swap" rel="stylesheet">
<style>
  :root {
    --page: #ffffff;
    --card-light: #ffffff;
    --card-shade: #e3e3e4;
    --panel: #58585a;
    --orange: #f07f1a;
    --orange-deep: #e8700f;
    --silver-light: #f2f2f2;
    --silver-dark: #9c9c9e;
    --brand-grey: #8a8a8c;
    --text-light: #ffffff;
  }
  html, body {
    margin: 0;
    width: 1200px;
    height: 900px;
    overflow: hidden;
    background: var(--page);
  }
  .business-card {
    position: absolute;
    left: 200px;
    top: 210px;
    width: 820px;
    height: 490px;
    overflow: hidden;
    background: radial-gradient(ellipse at 10% 15%, var(--card-shade) 0%, var(--card-light) 65%);
    font-family: "Cinzel", serif;
  }
  .card-swoosh {
    position: absolute;
    inset: 0;
    width: 820px;
    height: 490px;
  }
  .brand-name {
    position: absolute;
    left: 70px;
    top: 104px;
    margin: 0;
    font-family: "Cinzel", serif;
    font-weight: 600;
    font-size: 34px;
    letter-spacing: 1px;
    color: var(--brand-grey);
  }
  .contact-block {
    position: absolute;
    left: 340px;
    top: 296px;
    color: var(--text-light);
  }
  .contact-name {
    margin: 0 0 22px;
    font-size: 22px;
    font-weight: 400;
    color: var(--orange);
  }
  .contact-role {
    font-size: 17px;
  }
  .contact-line {
    margin: 0;
    font-size: 18px;
    line-height: 24px;
    letter-spacing: 0.3px;
  }
  .label {
    color: var(--orange);
  }
</style>
</head>
<body>
  <div class="business-card">
    <svg class="card-swoosh" viewBox="0 0 820 490" aria-hidden="true">
      <defs>
        <linearGradient id="silverEdge" x1="0" y1="1" x2="1" y2="0">
          <stop offset="0" stop-color="var(--silver-dark)"/>
          <stop offset="0.45" stop-color="var(--silver-light)"/>
          <stop offset="1" stop-color="var(--silver-dark)"/>
        </linearGradient>
        <linearGradient id="orangeEdge" x1="0" y1="1" x2="1" y2="0">
          <stop offset="0" stop-color="var(--orange-deep)"/>
          <stop offset="1" stop-color="var(--orange)"/>
        </linearGradient>
      </defs>
      <path class="swoosh-orange" fill="url(#orangeEdge)"
            d="M92 490 C150 290 400 176 820 176 L820 490 Z"/>
      <path class="swoosh-silver" fill="url(#silverEdge)"
            d="M116 490 C184 306 420 192 820 182 L820 490 Z"/>
      <path class="swoosh-panel" fill="var(--panel)"
            d="M150 490 C218 322 440 206 820 190 L820 490 Z"/>
    </svg>

    <p class="brand-name">Trevik Builders</p>

    <div class="contact-block">
      <p class="contact-name">Marlo Venturi <span class="contact-role">- Director</span></p>
      <p class="contact-line"><span class="label">ABN:</span> 47 305 921 276 | BAS LIC 6825170</p>
      <p class="contact-line"><span class="label">Ph:</span> 07 4651 2839 | <span class="label">Fax:</span> 07 4651 2840</p>
      <p class="contact-line"><span class="label">Email:</span> trevikbuilders@quillpost.net</p>
      <p class="contact-line"><span class="label">Address:</span> PO Box 5087, Corrabeen, Qld, 4286</p>
    </div>
  </div>
</body>
</html>
```